Business Card Design for Financial Services Company
Coin Harbor
Project: Business Card Design for Financial Services Company
Industry: Financial Services
Business Card Design for Financial Services Company - Financial Services
Creative Brief
Bright & Fun-filled
Marcus T. Holloway
President & CEO
2384 Avenue K
Brooklyn, New York 11487
marcus@CoinHarbor.example
http://www.CoinHarbor.example
1) I am uploading the logo. The logo is a combination of text and an image. When creating business card designs, you may place the "Coin Harbor" to the left, right, below, or above the logo. The logo can be anywhere in relation to the text "Coin Harbor". It is entirely up to you. I would like to see your creativity.
2) The business card needs to have the following fields:
Phone
Fax
Toll Free Phone
Toll Free Fax
Mobile Phone
E-mail
Website
I have entered temporary contact information. I will provide the correct contact information after the winning design has been selected.
3) Please do not submit complete stationary designs. I am only looking for business card designs. After the business card design has been selected, we will use that design to create the remaining stationary.
Please contact me with any questions that you may have.
Thank you, and good luck.
Thank you to all of the designers that have submitted designs in this project. I will select the winner of the contest within 4 days.
I have increased the contest prize to $100.00. In addition, I will also provide the winning designer with a donation. The contest was ending in a few hours so I have extended it by 2 days because I thought of a design that I think would look nice and I would like to provide you with the opportunity of submitting more designs. Here is the design that I would like to see:
(1) some very small green dollar bills floating around
(2) some very small green dollar bills piled up on the bottom
(3) some very small green dollar bills floating around and also piled up on the bottom
(4) anything else that you can think of
Can you please submit a few variations of such designs?
Dear Designers: I'm going to be reviewing the submissions when the contest is over in about 2 days. I have an idea that I think would be nice. How about some type of a design where there are: (1) some very small green dollar bills floating around; or (2) some very small green dollar bills piled up on the bottom; or (3) some very small green dollar bills floating around and also piled up on the bottom. Can someone please submit a few variations of such designs? Also, in addition to the contest award, I will also be providing the winning designer with a donation. Thank you.
A few designers have sent me emails telling me that they wanted to submit more designs but that the contest has already ended. As such, I have extended the contest by an additional 3 days to allow a few designers to submit more designs.
Dear All Designers: Please only upload business card designs with a front view. When you upload designs from a side view or you put the designs on top of something, it is very difficult to see the detail in the designs. Also, please be sure to only upload business card designs. When a winning business card design has been selected, the winning design can be applied to the rest of the stationary. Thank you.

```html
<!DOCTYPE html>
<html lang="en">
<head>
<meta charset="utf-8">
<title>Coin Harbor – Business Card</title>
<link href="https://fonts.googleapis.com/css2?family=Open+Sans:wght@400;600;700&display=swap" rel="stylesheet">
<style>
  :root {
    --backdrop: #0b1a12;
    --card: #ffffff;
    --green-dark: #1d7a3a;
    --green-name: #2f7d3a;
    --green-light: #7db356;
    --green-band-end: #15873f;
    --bills: #cfe6c4;
    --ink: #222222;
    --rule: #6aa86a;
  }
  * { margin: 0; padding: 0; box-sizing: border-box; }
  html, body { width: 1200px; height: 844px; overflow: hidden; }
  body { background: var(--backdrop); font-family: "Open Sans", Arial, sans-serif; position: relative; }

  .card {
    position: absolute; left: 151px; top: 166px;
    width: 898px; height: 513px;
    background: var(--card); overflow: hidden;
  }

  .brand { position: absolute; left: 0; width: 478px; top: 210px; text-align: center; }
  .brand-dot {
    width: 86px; height: 86px; border-radius: 50%;
    background: var(--green-dark); margin: 0 auto 26px;
  }
  .brand-name {
    font-weight: 700; font-size: 38px; letter-spacing: 2px;
    color: var(--green-dark); text-transform: uppercase; line-height: 1;
  }
  .brand { top: 180px; }

  .bill-pile {
    position: absolute; left: 0; top: 360px; width: 396px; height: 153px;
    background: linear-gradient(160deg, rgba(207,230,196,0.3) 0%, var(--bills) 60%, #b9dbac 100%);
    clip-path: polygon(0 0, 18% 8%, 45% 40%, 80% 45%, 100% 60%, 100% 100%, 0 100%);
  }

  .divider {
    position: absolute; left: 480px; top: 63px; width: 2px; height: 331px;
    background: linear-gradient(to bottom, rgba(106,168,106,0.3), var(--rule), rgba(106,168,106,0.3));
  }

  .person { position: absolute; left: 510px; top: 66px; }
  .person-name { font-size: 27px; font-weight: 400; color: var(--green-name); line-height: 1.1; letter-spacing: -0.3px; }
  .person-title { font-size: 19px; color: var(--ink); line-height: 1.2; }

  .address { position: absolute; left: 515px; top: 146px; font-size: 22px; color: var(--ink); line-height: 35px; }

  .contacts { position: absolute; left: 512px; top: 221px; list-style: none; }
  .contacts li { display: flex; align-items: center; height: 37px; font-size: 22px; color: var(--ink); }
  .contacts li.email { font-size: 19px; height: 32px; margin-top: 2px; }
  .contacts svg { width: 22px; height: 22px; margin-right: 10px; flex: none; fill: var(--green-dark); }

  .band {
    position: absolute; left: 285px; right: 0; bottom: 0; height: 40px;
    background: linear-gradient(to right, var(--green-light) 0%, var(--green-light) 55%, var(--green-band-end) 100%);
  }
  .website {
    position: absolute; right: 18px; bottom: 8px;
    font-size: 20px; color: #fff;
  }
</style>
</head>
<body>
  <div class="card">
    <div class="band"></div>
    <div class="bill-pile" role="img" aria-label="Pile of small green dollar bills scattered in the lower left corner"></div>

    <div class="brand">
      <div class="brand-dot"></div>
      <div class="brand-name">Coin Harbor</div>
    </div>

    <div class="divider"></div>

    <div class="person">
      <div class="person-name">Marcus T. Holloway</div>
      <div class="person-title">President &amp; CEO</div>
    </div>

    <div class="address">
      2384 Avenue K<br>
      Brooklyn, New York 11487
    </div>

    <ul class="contacts">
      <li><svg viewBox="0 0 24 24"><path d="M8 3c1 0 1.6.4 1.9 1.4l.8 2.6c.2.8-.1 1.5-.8 1.9l-1.2.7c.4 2.6 1.6 5 3.4 6.9l1.2-.5c.8-.3 1.6-.1 2 .6l1.5 2.3c.5.8.3 1.6-.5 2.2-1.3 1-3 1.3-4.4.3C7.6 18.7 5 13.8 5 8.3 5 5.6 6.2 3 8 3z"/></svg>(800) 555-0140</li>
      <li><svg viewBox="0 0 24 24"><path d="M8 3c1 0 1.6.4 1.9 1.4l.8 2.6c.2.8-.1 1.5-.8 1.9l-1.2.7c.4 2.6 1.6 5 3.4 6.9l1.2-.5c.8-.3 1.6-.1 2 .6l1.5 2.3c.5.8.3 1.6-.5 2.2-1.3 1-3 1.3-4.4.3C7.6 18.7 5 13.8 5 8.3 5 5.6 6.2 3 8 3z"/></svg>(800) 555-0146</li>
      <li><svg viewBox="0 0 24 24"><path d="M7 1h10a2 2 0 0 1 2 2v18a2 2 0 0 1-2 2H7a2 2 0 0 1-2-2V3a2 2 0 0 1 2-2zm0 2v15h10V3H7zm5 16.2a1 1 0 1 0 0 2 1 1 0 0 0 0-2z"/></svg>(212) 555-0131</li>
      <li><svg viewBox="0 0 24 24"><path d="M7 2h10v5H7zM4 8h16a2 2 0 0 1 2 2v7h-4v5H6v-5H2v-7a2 2 0 0 1 2-2zm4 8v4h8v-4H8zm1 1h6v1H9z"/></svg>(212) 555-0141</li>
      <li class="email"><svg viewBox="0 0 24 24"><path d="M2 5h20v14H2V5zm2 2v.4l8 5.4 8-5.4V7H4zm16 2.8l-8 5.4-8-5.4V17h16V9.8z"/></svg>marcus@CoinHarbor.example</li>
    </ul>

    <div class="website">www.CoinHarbor.example</div>
  </div>
</body>
</html>
```